My garage customisation company needs a business card

I need a business card design for my company "Shed Mavens"
I provide fully customised garage solutions for your previously cluttered, waste of space. My logo was just completed and can be provided if needed. I need the card to be clean, classy and eye catching.
Thank you

Target Market(s)

Men and Woman Home Owners

Industry/Entity Type

Business

Contact Information for Business Card

Rupert Dunwell
rupe@shedmavens.example
shedmavens.example

It's Time To Take Back Your Garage... From simple storage solutions to fully customised from the floor up, we've got you covered.

Requirements
Must have
• Logo
• Name
• Email Address
• Website
• Brief Description of what we do
Nice to have
• Back ground picture of Before and After

```html
<!DOCTYPE html>
<html lang="en">
<head>
<meta charset="UTF-8">
<title>Shed Mavens – Business Card</title>
<link rel="stylesheet" href="https://fonts.googleapis.com/css2?family=Arimo:wght@400;700&display=swap">
<style>
  :root {
    --bg: #cfcfcf;
    --orange: #f05a28;
    --white: #ffffff;
    --steel-light: #d9dadc;
    --steel-mid: #b9babd;
    --steel-dark: #9c9da1;
    --ink: #3a3a3c;
    --placeholder-grey: #85878c;
  }
  * { box-sizing: border-box; margin: 0; padding: 0; }
  html, body { width: 1200px; height: 1000px; overflow: hidden; }
  body {
    background: var(--bg);
    font-family: "Arimo", Arial, sans-serif;
    position: relative;
  }
  .card {
    position: absolute;
    left: 220px;
    width: 760px;
    height: 434px;
    overflow: hidden;
    box-shadow: 0 6px 18px rgba(0,0,0,0.25);
  }
  .card--front { top: 40px; background: var(--orange); }
  .card--back {
    top: 526px;
    background: linear-gradient(160deg, var(--steel-light) 0%, var(--steel-mid) 55%, var(--steel-dark) 100%);
  }

  /* Front */
  .front__accent-bar {
    position: absolute;
    left: 88px; top: 0;
    width: 26px; height: 240px;
    background: var(--white);
  }
  .front__icons {
    position: absolute;
    left: 93px; top: 162px;
    display: flex; flex-direction: column; gap: 18px;
  }
  .front__icons svg { width: 16px; height: 16px; display: block; }
  .front__contact {
    position: absolute;
    left: 134px; top: 158px;
    list-style: none;
    color: var(--white);
    font-size: 19px;
    line-height: 34px;
  }
  .front__identity {
    position: absolute;
    right: 52px; top: 56px;
    text-align: right;
    color: var(--white);
  }
  .front__name { font-size: 25px; font-weight: 700; }
  .front__role { font-size: 14px; margin-top: 6px; letter-spacing: 0.3px; }
  .front__illustration {
    position: absolute;
    right: 0; top: 170px;
    width: 150px; height: 130px;
    background: var(--placeholder-grey);
  }
  .front__divider {
    position: absolute;
    left: 0; right: 0; top: 300px;
    height: 10px;
    background: var(--white);
  }
  .front__band {
    position: absolute;
    left: 0; right: 0; top: 310px; bottom: 0;
    background: linear-gradient(170deg, var(--steel-light), var(--steel-mid));
    display: flex; align-items: center; justify-content: center;
    text-align: center;
    color: var(--ink);
    font-size: 15px;
    line-height: 22px;
    padding: 0 40px;
  }

  /* Back */
  .back__brand {
    position: absolute;
    inset: 0;
    display: flex; align-items: center; justify-content: center; gap: 16px;
  }
  .back__brand-mark {
    width: 34px; height: 34px;
    background: var(--orange);
  }
  .back__brand-name {
    font-size: 52px; font-weight: 700;
    color: var(--orange);
    letter-spacing: 1px;
  }
  .back__frame { position: absolute; inset: 0; }
</style>
</head>
<body>

  <section class="card card--front" aria-label="Business card front">
    <div class="front__accent-bar"></div>
    <div class="front__icons">
      <svg viewBox="0 0 16 16" aria-hidden="true"><rect x="1" y="3" width="14" height="10" fill="#f05a28"/><polyline points="1,3 8,9 15,3" fill="none" stroke="#ffffff" stroke-width="1.4"/></svg>
      <svg viewBox="0 0 16 16" aria-hidden="true"><circle cx="8" cy="8" r="7" fill="#f05a28"/><g fill="none" stroke="#ffffff" stroke-width="1"><ellipse cx="8" cy="8" rx="3" ry="7"/><line x1="1" y1="8" x2="15" y2="8"/><line x1="8" y1="1" x2="8" y2="15"/></g></svg>
    </div>
    <ul class="front__contact">
      <li>rupe@shedmavens.example</li>
      <li>shedmavens.example</li>
    </ul>
    <div class="front__identity">
      <p class="front__name">Rupert Dunwell</p>
      <p class="front__role">DESIGNATION</p>
    </div>
    <div class="front__illustration" role="img" aria-label="Illustration of a house with a garage door"></div>
    <div class="front__divider"></div>
    <div class="front__band">
      <p>It's time to take back your garage...<br>
      Offering a wide range of simple storage solutions to a fully customised garage<br>
      from the ground up - we've got you covered.</p>
    </div>
  </section>

  <section class="card card--back" aria-label="Business card back">
    <svg class="back__frame" viewBox="0 0 760 434" aria-hidden="true">
      <polyline points="40,404 720,404 720,40" fill="none" stroke="#f05a28" stroke-width="3"/>
    </svg>
    <div class="back__brand">
      <span class="back__brand-mark"></span>
      <span class="back__brand-name">Shed Mavens</span>
    </div>
  </section>

</body>
</html>
```